Web site design for news feed - Corvel Live

We need to design a webpage to promote our web scraping newsfeed (similar to pagewheel) the name of the business is "Corvel Live" ( a subsidiary of our company Corvel - see www.corvel-holdings.example for details, DO NOT BASE THAT WEBSITE ON YOUR DESIGN).

We are inspired by famous Economists, we are inspired by empirical data, accuracy, but importantly the site needs to portray our "new approach" to delivering functional and "boring" financial news flow (pagewheel)

Websites we like:

www.zolvo.example - love the graphics
www.pagewheel.example - love the functionality
http://www.marketdial.example/ - practical
http://www.wirepost.example/ - practical
http://www.quenbrix.example/en-us/default.aspx
www.ldg.example
http://www.harbortimes.example/
www.velto.example

Our logo is attached

We like black and white, artful, mabel tunn etc
Updates

Hi All, please bear in mind that this is a NEWS site (it will need space to post stories) - so whilst the visual aspect is really important, the functionally around the amount of stories we can post is important too.

think marketdial.example, www.pitcrest.example, www.ldg.example - but feel (creativity) is zolvo.example, pagewheel.example

thanks all for some great designs.

i will revert to those closest tomorrow.
in the meantime, please bear in mind that the vision of skylines and economists helps me get to the design immediately, it resonates better, it helps me visually decide. 
lastly, in terms of the news "spaces", i will need to have 6 "top stories" and then room for maybe 20 more headlines..the top stories will need a picture, the 20 others will not (just headline text).
Thanks everyone again

Industry/Entity Type

Financial

Font styles to use
Serif
Sans Serif

```html
<!DOCTYPE html>
<html lang="en">
<head>
<meta charset="utf-8">
<title>Corvel Live – Financial News</title>
<link rel="stylesheet" href="https://fonts.googleapis.com/css2?family=Arimo:wght@400;700&family=Open+Sans:wght@400;600;700&family=PT+Sans+Narrow:wght@700&display=swap">
<style>
  :root{
    --page:#ffffff;
    --header:#1e1e1e;
    --nav:#464646;
    --orange:#ef8f18;
    --orange-text:#e8821e;
    --dark:#131313;
    --grey-band:#484848;
    --footer:#151515;
    --green:#86b817;
    --link:#8d8df0;
    --headline:#5a5ab4;
    --muted:#8b8b8b;
    --button:#c9c9ec;
    --white:#ffffff;
    --ink:#111111;
  }
  *{box-sizing:border-box;margin:0;padding:0}
  html,body{width:1200px;height:1200px;overflow:hidden;background:var(--page)}
  body{position:relative;font-family:"Arimo",Arial,sans-serif}
  .abs{position:absolute}

  /* header */
  .site-header{left:240px;top:0;width:720px;height:110px;background:var(--header)}
  .brand{left:14px;top:14px;display:flex;align-items:flex-start;gap:12px}
  .brand-mark{width:34px;height:34px;background:var(--orange);margin-top:4px}
  .brand-name{font-family:"Open Sans",sans-serif;font-size:34px;line-height:32px;color:var(--muted);font-weight:400}
  .world-map{left:264px;top:6px;width:258px;height:96px;border-radius:6px;
    background:radial-gradient(ellipse at center,#e6e6e6 0%,#9a9a9a 55%,#1e1e1e 100%)}
  .tagline{right:18px;top:16px;text-align:right;font-family:"Open Sans",sans-serif;font-size:28px;line-height:30px;color:var(--muted)}
  .account{right:18px;top:94px;display:flex;gap:28px;font-size:9px;font-weight:700;color:var(--orange)}
  .account span::before{content:"";display:inline-block;width:6px;height:6px;border-radius:50%;background:var(--link);margin-right:6px}

  /* nav */
  .main-nav{left:240px;top:128px;width:720px;height:35px;background:var(--nav)}
  .main-nav a{position:absolute;top:6px;font-family:"PT Sans Narrow",sans-serif;font-weight:700;font-size:19px;letter-spacing:2.6px;color:var(--white);text-decoration:none}

  /* hero */
  .hero{left:240px;top:186px;width:720px;height:128px;background:var(--orange)}
  .hero-screen{left:26px;top:4px;width:286px;height:122px;background:#000;border-radius:6px;padding:5px;box-shadow:0 22px 16px -8px rgba(0,0,0,.55)}
  .hero-screen-fill{width:100%;height:100%;background:linear-gradient(180deg,#dfe7f2 0%,#f4f6f9 45%,#d6dde8 100%)}
  .hero-copy{left:337px;top:9px;width:363px;font-size:15.3px;line-height:16.3px;color:var(--white);text-align:justify}

  /* features */
  .features{left:240px;top:347px;width:720px;height:231px;background:var(--dark)}
  .feature-title{font-family:"Open Sans",sans-serif;font-size:14.5px;color:var(--white);font-weight:600}
  .feature-photo{width:121px;height:70px;border:4px solid var(--white);border-radius:6px}
  .feature-text{width:164px;font-size:8.6px;line-height:12.6px;font-weight:700;color:var(--green);text-align:justify}

  /* insight columns */
  .insights{left:240px;top:610px;width:720px;height:218px;background:var(--grey-band)}
  .insight-title{width:170px;text-align:center;font-family:"Open Sans",sans-serif;font-size:14.5px;line-height:13px;color:var(--white);font-weight:600}
  .insight-text{width:152px;font-size:8.6px;line-height:13px;color:var(--green);text-align:justify}
  .insight-label{font-size:8.3px;font-weight:700;color:var(--link)}
  .insight-box{width:168px;height:70px;border:1.5px solid #d8d8d8;border-radius:8px}

  /* financial flow */
  .flow-title{left:290px;top:845px;font-family:"Open Sans",sans-serif;font-size:15.5px;color:var(--orange-text)}
  .story-headline{width:256px;font-size:9.6px;line-height:14px;color:var(--headline);text-align:justify}
  .story-source{font-size:9.2px;color:var(--orange-text)}
  .story-body{width:256px;font-size:9.2px;line-height:14px;color:var(--ink);text-align:justify}
  .story-photo{width:158px;height:80px}
  .story-btn{width:80px;height:14px;background:var(--button);border-radius:7px 2px 7px 2px;font-size:9px;line-height:14px;padding-left:14px;color:var(--ink);box-shadow:4px 4px 3px rgba(0,0,0,.45)}

  /* footer */
  .site-footer{left:240px;top:1100px;width:720px;height:100px;background:var(--footer)}
  .footer-head{font-size:8.6px;font-weight:700;color:var(--orange)}
  .footer-links{list-style:none;font-size:8.8px;font-weight:700;color:var(--link)}
  .social-grid{left:31px;top:24px;width:78px;height:68px;background:#f2f2f2;display:grid;grid-template-columns:repeat(4,1fr);gap:3px;padding:3px}
  .social-grid span{background:#9c9c9c}
</style>
</head>
<body>

<header class="site-header abs">
  <div class="brand abs">
    <span class="brand-mark"></span>
    <span class="brand-name">Corvel<br>Live</span>
  </div>
  <div class="world-map abs" role="img" aria-label="White world map on dark background"></div>
  <div class="tagline abs">Financial<br>News</div>
  <div class="account abs"><span>Register</span><span>Login</span></div>
</header>

<nav class="main-nav abs">
  <a href="#" style="left:110px">Home</a>
  <a href="#" style="left:205px">Newspapers</a>
  <a href="#" style="left:367px">Webs</a>
  <a href="#" style="left:469px">Tv</a>
  <a href="#" style="left:557px">Others</a>
</nav>

<section class="hero abs">
  <div class="hero-screen abs"><div class="hero-screen-fill" role="img" aria-label="Monitor showing a spreadsheet of financial figures"></div></div>
  <p class="hero-copy abs">Lorem ipsum dolor sit amet, consectetur adipisicing elit, sed do eiusmod tempor incididunt ut labore et dolore magna aliqua. Ut enim ad minim veniam, quis nostrud exercitation ullamco laboris nisi ut aliquip ex ea commodo consequat. fugiat nulla pariatur. officia deserunt mollit anim id est laborum. unde omnis iste natus error sit voluptatem.</p>
</section>

<section class="features abs">
  <h2 class="feature-title abs" style="left:32px;top:32px">Statistics</h2>
  <div class="feature-photo abs" role="img" aria-label="Glowing orange data display over a dark blue grid" style="left:29px;top:57px;background:linear-gradient(160deg,#c2521e 0%,#6a2a3a 45%,#2a2f6a 100%)"></div>
  <p class="feature-text abs" style="left:32px;top:144px">Lorem ipsum dolor sit amet, consectetur adipisicing elit, sed do eiusmod tempor incididunt ut labore et dolore magna</p>

  <h2 class="feature-title abs" style="left:385px;top:32px">Markets</h2>
  <div class="feature-photo abs" role="img" aria-label="Stone columns of a stock exchange building" style="left:383px;top:57px;background:linear-gradient(120deg,#cfd3d8 0%,#8c939b 50%,#4a5058 100%)"></div>
  <p class="feature-text abs" style="left:385px;top:144px">Lorem ipsum dolor sit amet, consectetur adipisicing elit, sed do eiusmod tempor incididunt ut labore et dolore magna</p>
</section>

<section class="insights abs">
  <h2 class="insight-title abs" style="left:37px;top:17px">Economists</h2>
  <p class="insight-text abs" style="left:48px;top:42px">Lorem ipsum dolor sit amet, consectetur adipisicing elit, sed do eiusmod tempor incididunt ut labore et dolore magna aliqua. Ut enim ad minim veniam, quis nostrud</p>
  <p class="insight-label abs" style="left:48px;top:111px">Today: Dr Alan Brisk</p>
  <div class="insight-box abs" style="left:44px;top:135px"></div>

  <h2 class="insight-title abs" style="left:262px;top:17px">Flows</h2>
  <p class="insight-text abs" style="left:275px;top:42px">Lorem ipsum dolor sit amet, consectetur adipisicing elit, sed do eiusmod tempor incididunt ut labore et dolore magna aliqua. Ut enim ad minim veniam, quis nostrud</p>
  <p class="insight-label abs" style="left:275px;top:111px">Import from:</p>
  <div class="insight-box abs" style="left:271px;top:135px"></div>

  <h2 class="insight-title abs" style="left:501px;top:8px">Empirical<br>Data</h2>
  <p class="insight-text abs" style="left:503px;top:42px">Lorem ipsum dolor sit amet, consectetur adipisicing elit, sed do eiusmod tempor incididunt ut labore et dolore magna aliqua. Ut enim ad minim veniam, quis nostrud</p>
  <p class="insight-label abs" style="left:503px;top:111px">Case Study:</p>
  <div class="insight-box abs" style="left:499px;top:135px"></div>
</section>

<h2 class="flow-title abs">Financial Flow</h2>

<article>
  <p class="story-headline abs" style="left:289px;top:878px">China's short-term money rates fall as fiscal deposits improve cash flow.</p>
  <p class="story-source abs" style="left:289px;top:906px">Newsline ▸ 1 day ago</p>
  <p class="story-body abs" style="left:289px;top:921px">More than 1 trln yuan in fiscal deposits seen in Dec" Money rates seen stabilising at elevated levels in nearterm (Adds details)By Ren Haolin ...</p>
  <div class="story-photo abs" role="img" aria-label="Grey city skyline with a tall tower" style="left:582px;top:882px;background:linear-gradient(180deg,#b9bcc0 0%,#6f7378 60%,#2c2e31 100%)"></div>
  <div class="story-btn abs" style="left:788px;top:887px">Coments</div>
  <div class="story-btn abs" style="left:788px;top:911px">Rate</div>
  <div class="story-btn abs" style="left:788px;top:933px">More news...</div>
</article>

<article>
  <p class="story-headline abs" style="left:289px;top:992px">Great expectections about news from the Asia markets after tsunami.</p>
  <p class="story-source abs" style="left:289px;top:1020px">NP ▸ 1 hour ago</p>
  <p class="story-body abs" style="left:289px;top:1035px">Lorem ipsum dolor sit amet, consectetur adipisicing elit, sed do eiusmod tempor incididunt ut labore et dolore magna aliqua. velit esse cillum dolore eu fugiat nulla pariatur.</p>
  <div class="story-photo abs" role="img" aria-label="Black and white stormy sea" style="left:582px;top:994px;height:81px;background:linear-gradient(180deg,#d0d0d0 0%,#8a8a8a 45%,#3a3a3a 100%)"></div>
  <div class="story-btn abs" style="left:788px;top:1001px">Coments</div>
  <div class="story-btn abs" style="left:788px;top:1025px">Rate</div>
  <div class="story-btn abs" style="left:788px;top:1047px">More news...</div>
</article>

<footer class="site-footer abs">
  <p class="footer-head abs" style="left:31px;top:10px">Social Media</p>
  <div class="social-grid abs">
    <span></span><span></span><span></span><span></span>
    <span></span><span></span><span></span><span></span>
    <span></span><span></span><span></span><span></span>
    <span></span><span></span><span></span><span></span>
  </div>

  <p class="footer-head abs" style="left:232px;top:9px">Abou Us</p>
  <ul class="footer-links abs" style="left:232px;top:23px;line-height:15px">
    <li>Introduction</li><li>Ethos</li><li>Enterprises</li><li>Contact Us</li>
  </ul>

  <p class="footer-head abs" style="left:404px;top:8px">Portals</p>
  <ul class="footer-links abs" style="left:404px;top:24px;line-height:15.5px">
    <li>The Financial News</li><li>NYSM</li><li>Tokai</li><li>European markets</li>
  </ul>
</footer>

</body>
</html>
```